Social Media Graphics - Copperfield Loop

Create 6-7 individual social media graphics (square size) to encourage folks to join our online course, using either of the text below (only one set of text per graphic:

The Lantern Ridge Method
How to Create a 7-Figure Business From Scratch
Sign Up Today!

Or

The Lantern Ridge Method
Fast-track Your Way to a Multi-Million Business!
Sign Up Today!

For the color scheme of the graphics, use 1 or 2 colors in the color palette attached; or use any colors that look nice with their outfits; AVOID using red, white and blue altogether because it will look like an Independence Day (4th of July) graphic and we don’t want that; make sure the graphics appeal to both men and women

Make sure each graphic contains 1 of the 2 pics attached; and make sure one of the graphics is all TEXT only.

Target Market(s)

men and women looking to make more money

Industry/Entity Type

entrepreneurship

Requirements
Must have
• see the text document attached
Nice to have
• We are open to a nice color design; the color palette colors are not required, especially we don't want red, white and blue used together
Should not have
• AVOID using red, white and blue altogether because it will look like an Independence Day (4th of July) graphic and we dont want that

```html
<!DOCTYPE html>
<html lang="en">
<head>
<meta charset="utf-8">
<title>The Lantern Ridge Method – Sign Up</title>
<link rel="stylesheet" href="https://fonts.googleapis.com/css2?family=Montserrat:wght@400;700;800;900&display=swap">
<style>
  :root {
    --royal: #1f1fb3;
    --royal-deep: #16169a;
    --royal-dark: #10107a;
    --bar: #2323c4;
    --blush: #fde2e0;
    --cream: #fff1d6;
    --pill: #ffc4cf;
    --ink: #111111;
    --arrow: #f2b33d;
    --photo-a: #3b3a5c;
    --photo-b: #24244a;
  }
  * { margin: 0; padding: 0; box-sizing: border-box; }
  html, body { width: 1200px; height: 1200px; overflow: hidden; }
  body { font-family: "Montserrat", sans-serif; background: var(--royal); }
  .graphic {
    position: relative;
    width: 1200px;
    height: 1200px;
    overflow: hidden;
  }
  .money-backdrop {
    position: absolute;
    inset: 0;
    background: radial-gradient(ellipse at 50% 40%, var(--royal) 0%, var(--royal-deep) 65%, var(--royal-dark) 100%);
  }
  .chart {
    position: absolute;
    inset: 0;
  }
  .headline {
    position: absolute;
    top: 82px;
    left: 0;
    width: 100%;
    text-align: center;
    font-weight: 900;
    font-size: 100px;
    line-height: 1.22;
    letter-spacing: 1px;
    color: var(--blush);
    text-transform: uppercase;
  }
  .headline .accent { color: var(--cream); }
  .subhead {
    position: absolute;
    top: 328px;
    left: 0;
    width: 100%;
    text-align: center;
    font-size: 36px;
    font-weight: 400;
    line-height: 1.3;
    color: var(--cream);
  }
  .subhead strong { font-weight: 700; }
  .cta {
    position: absolute;
    top: 456px;
    left: 381px;
    width: 438px;
    height: 92px;
    border-radius: 46px;
    background: var(--pill);
    color: var(--ink);
    font-weight: 800;
    font-size: 38px;
    display: flex;
    align-items: center;
    justify-content: center;
  }
  .hosts-photo {
    position: absolute;
    left: 250px;
    top: 610px;
    width: 700px;
    height: 590px;
    background: linear-gradient(180deg, var(--photo-a) 0%, var(--photo-b) 100%);
    border-radius: 220px 220px 0 0;
  }
</style>
</head>
<body>
  <main class="graphic">
    <div class="money-backdrop" role="img" aria-label="Blue-toned backdrop of scattered falling dollar bills"></div>

    <svg class="chart" width="1200" height="1200" viewBox="0 0 1200 1200" aria-hidden="true">
      <rect class="chart-bar" x="83" y="967" width="140" height="233" fill="var(--bar)"/>
      <rect class="chart-bar" x="775" y="700" width="110" height="500" fill="var(--bar)"/>
      <rect class="chart-bar" x="961" y="522" width="140" height="678" fill="var(--bar)"/>
      <path class="growth-arrow" d="M90 912 C 420 860, 800 720, 1050 420" fill="none" stroke="var(--arrow)" stroke-width="12" stroke-linecap="round"/>
      <polygon class="growth-arrow-head" points="1108,358 1080,488 1048,420 978,416" fill="var(--arrow)"/>
    </svg>

    <h1 class="headline">The <span class="accent">Lantern</span><br>Ridge Method</h1>

    <p class="subhead">How to Create a <strong>7-Figure Business</strong><br>From Scratch</p>

    <div class="cta">Sign Up Today!</div>

    <div class="hosts-photo" role="img" aria-label="Photo of the two course hosts, a man in a black turtleneck with arms crossed and a woman in a teal denim blazer, both smiling"></div>
  </main>
</body>
</html>
```